Brill Insurance Agency - Business Cards

Hello, I am needing new trendy business cards for our Insurance Agency now that I have a new Logo. I have attached our new logo with several color options along with a business card design that I like. I am leaning towards burgundy and blue colors. I have attached our current business card. I have also attached a headshot of our company president, Martin Vale, that you can use if you wish. Thank you so much in advance for all the wonderful designs!!!!

Target Market(s)

We want to look very professional to potential customers and we also want to look very professional so insurance companies will want to contract with us to sell their product.

Industry/Entity Type

Insurance

Contact Information for Business Card

Martin Vale
mvale@brillagency.com
Business: 555-213-4087
Fax: 555-213-7751
Cell: 555-390-2618
Toll Free: 888-555-0194
42 W Elm Rd Butler, MO 64730
www.brillagency.net

Font styles to use
Serif
Sans Serif

Colors
0355a3
3277b5
f04a50
ec1f27

Requirements
Nice to have
• I love creativity. The more creative and balanced a business card design the more I will like it. I would like the card to be printed horizontally instead of vertically.
Should not have
• My project should not have the Allied Coverage Network logo. It is no longer used in the industry.

```html
<!DOCTYPE html>
<html lang="en">
<head>
<meta charset="utf-8">
<title>Brill Insurance Agency – Business Cards</title>
<link rel="stylesheet" href="https://fonts.googleapis.com/css2?family=League+Spartan:wght@600&family=Exo+2:wght@300&display=swap">
<style>
  :root {
    --page: #f4f5f7;
    --card-core: #2b74b0;
    --card-edge: #1d3a55;
    --cream: #fdf3d3;
    --link-blue: #3a7ab0;
    --icon-ink: #1e3a55;
  }
  * { box-sizing: border-box; margin: 0; padding: 0; }
  html, body { width: 993px; height: 1200px; overflow: hidden; background: var(--page); }
  body { position: relative; font-family: "Exo 2", sans-serif; color: var(--cream); }

  .card {
    position: absolute;
    left: 39px; width: 910px; height: 520px;
    background: radial-gradient(ellipse 62% 70% at 50% 52%, var(--card-core) 0%, #24567f 55%, var(--card-edge) 100%);
    overflow: hidden;
  }
  .card--front { top: 56px; }
  .card--back { top: 630px; }

  .abs { position: absolute; }

  /* front */
  .brand-dot { left: 83px; top: 185px; width: 154px; height: 154px; border: 11px solid var(--cream); border-radius: 50%; }
  .brand-divider { left: 298px; top: 171px; width: 3px; height: 178px; background: var(--cream); }
  .brand-name {
    left: 324px; top: 221px; width: 520px;
    font-family: "League Spartan", sans-serif; font-weight: 600;
    font-size: 57px; line-height: 1; letter-spacing: 3.5px; white-space: nowrap;
  }
  .brand-sub {
    left: 324px; top: 273px; width: 504px;
    display: flex; align-items: center; gap: 10px;
    font-family: "League Spartan", sans-serif; font-weight: 600;
    font-size: 37px; line-height: 1; letter-spacing: 9px; white-space: nowrap;
  }
  .brand-sub .rule { flex: 1; height: 3px; background: var(--cream); }

  /* back */
  .person-name {
    left: 32px; top: 38px;
    font-family: "League Spartan", sans-serif; font-weight: 600;
    font-size: 42px; line-height: 1; letter-spacing: 1.5px; white-space: nowrap;
  }
  .person-title {
    left: 58px; top: 80px; width: 266px;
    display: flex; align-items: center; gap: 12px;
    font-family: "League Spartan", sans-serif; font-weight: 600; font-size: 31px; line-height: 1;
  }
  .person-title .rule { flex: 1; height: 3px; background: var(--cream); }

  .contact { left: 32px; display: flex; align-items: flex-start; gap: 8px; font-size: 21px; line-height: 26px; white-space: nowrap; }
  .contact .icon { width: 28px; height: 28px; border-radius: 50%; background: var(--cream); flex: none; display: flex; align-items: center; justify-content: center; }
  .contact--mail { top: 164px; }
  .contact--phone { top: 218px; }
  .contact--place { top: 352px; }

  .emblem-ring { left: 512px; top: 108px; width: 274px; height: 274px; border: 17px solid var(--cream); border-radius: 50%; }

  .web-band {
    left: 0; bottom: 0; width: 100%; height: 43px; background: var(--cream);
    color: var(--link-blue); font-size: 18px; text-align: center; line-height: 43px; letter-spacing: 0.5px;
  }
</style>
</head>
<body>
  <section class="card card--front">
    <div class="abs brand-dot"></div>
    <div class="abs brand-divider"></div>
    <div class="abs brand-name">BRILL INSURANCE</div>
    <div class="abs brand-sub"><span class="rule"></span><span>AGENCY INC</span><span class="rule"></span></div>
  </section>

  <section class="card card--back">
    <div class="abs person-name">MARTIN VALE</div>
    <div class="abs person-title"><span class="rule"></span><span>CEO</span><span class="rule"></span></div>

    <div class="abs contact contact--mail">
      <span class="icon"><svg width="18" height="13" viewBox="0 0 18 13"><rect x="1" y="1" width="16" height="11" fill="none" stroke="#1e3a55" stroke-width="1.6"/><path d="M1 1 L9 7.5 L17 1" fill="none" stroke="#1e3a55" stroke-width="1.6"/></svg></span>
      <span>mvale@brillagency.com</span>
    </div>

    <div class="abs contact contact--phone">
      <span class="icon"><svg width="18" height="12" viewBox="0 0 18 12"><path d="M1 5 Q9 -1 17 5 L15 8 L12 6.5 L12 4.5 Q9 3.5 6 4.5 L6 6.5 L3 8 Z" fill="#1e3a55"/></svg></span>
      <span>Business: 555-213-4087<br>Fax: 555-213-7751<br>Cell: 555-390-2618<br>Toll Free: 888-555-0194</span>
    </div>

    <div class="abs contact contact--place">
      <span class="icon" style="width:30px;height:30px;"><svg width="14" height="19" viewBox="0 0 14 19"><path d="M7 18 C3 12 1 9 1 6.5 A6 6 0 0 1 13 6.5 C13 9 11 12 7 18 Z" fill="#1e3a55"/><circle cx="7" cy="6.5" r="2.3" fill="#fdf3d3"/></svg></span>
      <span>42 W Elm Rd Fairbrook, MO 64999</span>
    </div>

    <div class="abs emblem-ring"></div>

    <div class="abs web-band">www.brillagency.net</div>
  </section>
</body>
</html>
```